Corvane Lending Partners. Professional and Established Company

A full service finance company specializing in obtaining capital for small business. Business Lending advisor, helping small business owners access the capital they need to launch, grow, or sustain their business. Many of our programs offer flexible guidelines to overcome common obstacles such as credit score, credit history, and time in business, financials, and industry type. Our streamlined funding process makes getting a business loan, business line of credit, stated income commercial real estate loan, a smooth and stress free experience.SOME OF THE MOST COMMON NEEDS FOR BUSINESS CAPITAL:• Working Capital• Debt Consolidations (loans, merchant cash advances, etc.)• Payroll• Operating Expenses• Inventory• Equipment Financing• Commercial Real Estate (Purchase, Fix & Flip, Rehab, Renovations)• Business Acquisitions• Business ExpansionWe like the websites:www.brookfellcap.com they are in the same industry and provide the same servicesWe are wanting to be able to update when we do press releases and such using Word Press. Our look should be very professional and we will be adding Our Team Professional Bios and Headshots.

Industry/Entity Type

Finance

Number of Pages Required

5+ page

Font styles to use
Serif
Sans Serif

Requirements
Must have
• We want to copy brookfellcap.com
• We need:
• Home Page
• About Us
• Loan Programs
• Loan Criteria
• News
• Apply Now
• Contact
Nice to have
• See brookfellcap.com
Should not have
• Need professional design. Nothing bright or abstract

```html
<!DOCTYPE html>
<html lang="en">
<head>
<meta charset="utf-8">
<title>Corvane Lending Partners</title>
<link rel="stylesheet" href="https://fonts.googleapis.com/css2?family=Open+Sans:wght@400;600;700&family=Lora:wght@400;600&display=swap">
<style>
:root{
  --blue:#1f72b8;
  --navy:#1b3a66;
  --slate:#3d4753;
  --ink:#2b2f36;
  --muted:#6b7380;
  --line:#dfe3e8;
  --white:#ffffff;
}
*{box-sizing:border-box;margin:0;padding:0}
html,body{width:1200px;height:3236px;overflow:hidden}
body{font-family:"Open Sans",Arial,sans-serif;color:var(--ink);background:var(--white);position:relative}
a{color:inherit;text-decoration:none}

.site-header{height:88px;position:relative;background:var(--white)}
.brand{position:absolute;left:24px;top:24px;display:flex;align-items:center;gap:10px}
.brand-mark{width:14px;height:14px;background:var(--navy)}
.brand-name{font-family:"Lora",Georgia,serif;font-weight:600;font-size:24px;color:var(--navy);letter-spacing:.5px}
.top-contact{position:absolute;right:28px;top:14px;display:flex;gap:26px;font-size:11px;color:var(--muted)}
.top-contact span{display:flex;align-items:center;gap:6px}
.main-nav{position:absolute;right:28px;top:50px;display:flex;gap:30px;font-size:13px;color:var(--ink)}
.main-nav a.active{color:var(--blue);border-bottom:2px solid var(--blue);padding-bottom:4px}

.hero{position:relative;height:664px;background:linear-gradient(180deg,#5d6f86 0%,#3a4b62 45%,#233048 75%,#1a2334 100%)}
.hero-copy{position:absolute;left:100px;top:292px;color:var(--white);width:460px}
.hero-title{font-family:"Lora",Georgia,serif;font-weight:400;font-size:40px;line-height:1.1}
.hero-sub{font-size:19px;line-height:1.4;margin-top:20px}
.btn-apply{display:inline-block;margin-top:30px;background:var(--blue);color:var(--white);font-size:11px;font-weight:700;padding:9px 22px;border-radius:3px;letter-spacing:.5px}
.closed-title{position:absolute;left:0;right:0;top:532px;text-align:center;color:var(--white);font-size:20px}
.closed-strip{position:absolute;left:40px;right:40px;top:580px;display:grid;grid-template-columns:repeat(6,1fr);border-top:1px solid rgba(255,255,255,.35);padding-top:12px}
.closed-item{text-align:center;color:var(--white);font-size:11px;line-height:1.5}
.closed-item b{display:block;font-weight:600}

.video-cta{height:128px;text-align:center;padding-top:28px}
.video-cta a{color:var(--blue);font-weight:700;font-size:21px;text-decoration:underline}
.video-cta p{font-weight:600;font-size:18px;margin-top:2px}

.feature{display:grid;height:312px}
.feature-about{grid-template-columns:660px 540px}
.feature-news{grid-template-columns:540px 660px;height:320px}
.feature-text{color:var(--white);padding:56px 40px 0 48px}
.feature-about .feature-text{background:var(--blue)}
.feature-news .feature-text{background:var(--slate)}
.eyebrow{font-size:10px;font-weight:700;letter-spacing:.5px}
.feature-text h2{font-size:21px;font-weight:700;line-height:1.3;margin-top:12px;max-width:470px}
.feature-text p{font-size:13px;line-height:1.5;margin-top:14px;max-width:480px}
.more{display:inline-block;font-size:10px;font-weight:700;margin-top:14px;letter-spacing:.5px}
.photo{display:block}
.photo-villa{background:linear-gradient(160deg,#a7c9e6 0%,#d7dfe2 40%,#7fa6a4 70%,#5b7a6c 100%)}
.photo-building{background:linear-gradient(170deg,#cfe0ee 0%,#e8e2d6 45%,#8d9a78 75%,#4f6a45 100%)}

.programs{padding-top:72px}
.programs h3{text-align:center;color:var(--blue);font-size:19px;font-weight:600;letter-spacing:.5px}
.program-grid{display:grid;grid-template-columns:repeat(3,398px);column-gap:3px;margin-top:46px;row-gap:0}
.program{height:452px}
.program .photo{height:288px}
.program h4{text-align:center;font-size:14px;font-weight:700;margin-top:24px}
.program p{text-align:center;font-size:11px;line-height:1.55;color:var(--muted);width:230px;margin:10px auto 0}
.ph-land{background:linear-gradient(180deg,#b9cfe3 0%,#c9d3b5 45%,#7f9a52 100%)}
.ph-hotel{background:linear-gradient(180deg,#7c8590 0%,#a89a88 50%,#5c5146 100%)}
.ph-multi{background:linear-gradient(180deg,#9cc0e0 0%,#d8d3c8 50%,#6d8a66 100%)}
.ph-office{background:linear-gradient(180deg,#8fb8df 0%,#b5c7d6 55%,#6a8090 100%)}
.ph-mixed{background:linear-gradient(180deg,#2d4d8a 0%,#8a6a55 55%,#c58b4a 100%)}
.ph-retail{background:linear-gradient(180deg,#d8c9b0 0%,#b59a74 50%,#6e5a44 100%)}
.ph-industrial{background:linear-gradient(180deg,#7fa7d4 0%,#c0c9d2 50%,#8c949c 100%)}
.ph-warehouse{background:linear-gradient(180deg,#5f6c7c 0%,#8e8a7a 50%,#4b5561 100%)}
.ph-storage{background:linear-gradient(180deg,#c7ccd2 0%,#8898ab 50%,#3f5370 100%)}
.all-programs{text-align:center;margin-top:2px}
.all-programs a{display:inline-block;border:1px solid var(--blue);color:var(--blue);font-size:10px;font-weight:600;padding:9px 30px;letter-spacing:.5px}

.site-footer{position:absolute;left:0;right:0;top:3100px;height:136px;border-top:1px solid var(--line)}
.site-footer .brand{top:24px}
.site-footer .main-nav{top:36px}
.copyright{position:absolute;left:0;right:0;bottom:0;height:40px;background:var(--navy);color:#c8d3e3;font-size:11px;text-align:center;line-height:40px}
</style>
</head>
<body>

<header class="site-header">
  <a class="brand" href="#"><span class="brand-mark"></span><span class="brand-name">Corvane Lending Partners</span></a>
  <div class="top-contact">
    <span><svg width="11" height="11" viewBox="0 0 24 24"><path fill="#1f72b8" d="M6.6 10.8a15 15 0 0 0 6.6 6.6l2.2-2.2c.3-.3.7-.4 1-.2 1.1.4 2.3.6 3.6.6.6 0 1 .4 1 1V20c0 .6-.4 1-1 1A17 17 0 0 1 3 4c0-.6.4-1 1-1h3.5c.6 0 1 .4 1 1 0 1.3.2 2.5.6 3.6.1.3 0 .7-.2 1z"/></svg>+1 (555) 014-2280</span>
    <span><svg width="12" height="10" viewBox="0 0 24 18"><rect x="1" y="1" width="22" height="16" rx="2" fill="none" stroke="#1f72b8" stroke-width="2"/><path d="M1 2l11 8 11-8" fill="none" stroke="#1f72b8" stroke-width="2"/></svg>info@corvanelending.com</span>
  </div>
  <nav class="main-nav">
    <a class="active" href="#">Home</a><a href="#">About Us</a><a href="#">Loan Programs</a><a href="#">Loan Criteria</a><a href="#">News</a><a href="#">Apply Now</a><a href="#">Contact Us</a>
  </nav>
</header>

<section class="hero" role="img" aria-label="Dusk photograph of a large luxury residence with lit windows and a pool">
  <div class="hero-copy">
    <h1 class="hero-title">Corvane Lending Partners</h1>
    <p class="hero-sub">The nation's most unique private lender to the commercial real estate market.</p>
    <a class="btn-apply" href="#">APPLY NOW</a>
  </div>
  <h2 class="closed-title">Recently Closed Loans</h2>
  <div class="closed-strip">
    <div class="closed-item"><b>Office Building</b>Columbus, OH $2.4M</div>
    <div class="closed-item"><b>Industrial Warehouse</b>Dallas, TX $5.1M</div>
    <div class="closed-item"><b>Retail Center</b>Tampa, FL $3.8M</div>
    <div class="closed-item"><b>Multifamily Complex</b>Denver, CO $7.2M</div>
    <div class="closed-item"><b>Mixed-Use Property</b>Phoenix, AZ $4.6M</div>
    <div class="closed-item"><b>Self Storage</b>Austin, TX $1.9M</div>
  </div>
</section>

<section class="video-cta">
  <a href="#">Click Here</a>
  <p>for a comprehensive video of our services.</p>
</section>

<section class="feature feature-about">
  <div class="feature-text">
    <span class="eyebrow">ABOUT US</span>
    <h2>There are many variations of passages of Lorem Ipsum available.</h2>
    <p>There are many variations of passages of Lorem Ipsum available, but the majority have suffered alteration in some form, by injected humour, or randomised words which don't look even slightly believable. If you are going to use a passage of Lorem...</p>
    <a class="more" href="#">DISCOVER MORE ABOUT</a>
  </div>
  <div class="photo photo-villa" role="img" aria-label="Photograph of a modern white villa with a pool and palm trees"></div>
</section>

<section class="feature feature-news">
  <div class="photo photo-building" role="img" aria-label="Photograph of a modern residential building with landscaped gardens"></div>
  <div class="feature-text">
    <span class="eyebrow">RECENT NEWS</span>
    <h2>There are many variations of passages of Lorem Ipsum available.</h2>
    <p>There are many variations of passages of Lorem Ipsum available, but the majority have suffered alteration in some form, by injected humour, or randomised words which don't look even slightly believable. If you are going to use a passage of Lorem...</p>
    <a class="more" href="#">READ MORE</a>
  </div>
</section>

<section class="programs">
  <h3>LOAN PROGRAMS</h3>
  <div class="program-grid">
    <article class="program"><div class="photo ph-land" role="img" aria-label="Photograph of open farmland under a blue sky"></div><h4>Land Loans</h4><p>There are many variations of passages of Lorem Ipsum available but the majority have suffered...</p></article>
    <article class="program"><div class="photo ph-hotel" role="img" aria-label="Photograph of a hotel lobby interior"></div><h4>Hospitality Loans</h4><p>There are many variations of passages of Lorem Ipsum available but the majority have suffered...</p></article>
    <article class="program"><div class="photo ph-multi" role="img" aria-label="Photograph of a multifamily residential building"></div><h4>Multifamily Loans</h4><p>There are many variations of passages of Lorem Ipsum available but the majority have suffered...</p></article>
    <article class="program"><div class="photo ph-office" role="img" aria-label="Photograph of a glass office building"></div><h4>Office Loans</h4><p>There are many variations of passages of Lorem Ipsum available but the majority have suffered...</p></article>
    <article class="program"><div class="photo ph-mixed" role="img" aria-label="Photograph of a mixed-use street at dusk"></div><h4>Mixed-Use Loans</h4><p>There are many variations of passages of Lorem Ipsum available but the majority have suffered...</p></article>
    <article class="program"><div class="photo ph-retail" role="img" aria-label="Photograph of a shopping mall interior"></div><h4>Retail Loans</h4><p>There are many variations of passages of Lorem Ipsum available but the majority have suffered...</p></article>
    <article class="program"><div class="photo ph-industrial" role="img" aria-label="Photograph of an industrial plant with silos"></div><h4>Industrial Loans</h4><p>There are many variations of passages of Lorem Ipsum available but the majority have suffered...</p></article>
    <article class="program"><div class="photo ph-warehouse" role="img" aria-label="Photograph of warehouse shelving stocked with goods"></div><h4>Warehouse Loans</h4><p>There are many variations of passages of Lorem Ipsum available but the majority have suffered...</p></article>
    <article class="program"><div class="photo ph-storage" role="img" aria-label="Photograph of a self storage corridor with roll-up doors"></div><h4>Self Storage Loans</h4><p>There are many variations of passages of Lorem Ipsum available but the majority have suffered...</p></article>
  </div>
  <div class="all-programs"><a href="#">ALL LOAN PROGRAMS</a></div>
</section>

<footer class="site-footer">
  <a class="brand" href="#"><span class="brand-mark"></span><span class="brand-name">Corvane Lending Partners</span></a>
  <nav class="main-nav">
    <a class="active" href="#">Home</a><a href="#">About Us</a><a href="#">Loan Programs</a><a href="#">Loan Criteria</a><a href="#">News</a><a href="#">Apply Now</a><a href="#">Contact Us</a>
  </nav>
  <div class="copyright">© 2024 Corvane Lending Partners. All Rights Reserved.</div>
</footer>

</body>
</html>
```